Harborline Cremations Business Cards

To create a business card for my company Harborline Cremations. Remember it is a cremation company.
We want to make sure people have a business card and information. Something modern, professional
100% Online
Prices starting at $695 all-inclusive (prices subject to change without notice).
A business card is the first point of contact with the prospective client.

Contact Information for Business Card

(305) 418-7260
www.HarborlineCremationsMiami.example
harborlinecremations@mailbox.example

Requirements
Must have
• 100% Online
Prices starting at $695 all-inclusive (prices subject to change without notice)

(305) 418-7260

Must match logo style
Should not have
• No black backgrounds. Please only use the white, orange and blue from the logo

```html
<!DOCTYPE html>
<html lang="en">
<head>
<meta charset="utf-8">
<title>Harborline Cremations – Business Card</title>
<link rel="stylesheet" href="https://fonts.googleapis.com/css2?family=Lato:wght@400;700;900&display=swap">
<style>
  :root {
    --stage: #ece7e1;
    --card: #fbfbf9;
    --card-edge: #e3dfd9;
    --teal: #1a8db0;
    --orange: #e7862b;
    --ink: #5a636c;
    --muted: #8a9199;
  }
  * { margin: 0; padding: 0; box-sizing: border-box; }
  html, body {
    width: 1200px;
    height: 1047px;
    overflow: hidden;
    background: var(--stage);
    font-family: "Lato", Arial, sans-serif;
  }
  .business-card {
    position: absolute;
    left: 128px;
    top: 267px;
    width: 944px;
    height: 513px;
    background: var(--card);
    border: 1px solid var(--card-edge);
    border-radius: 18px;
    overflow: hidden;
    box-shadow: 0 12px 34px rgba(80, 60, 40, 0.12);
  }
  .brand-name {
    position: absolute;
    left: 62px;
    top: 84px;
    font-size: 46px;
    font-weight: 700;
    letter-spacing: 0.08em;
    text-transform: uppercase;
    color: var(--teal);
    line-height: 1;
  }
  .person-name {
    position: absolute;
    left: 64px;
    top: 246px;
    font-size: 37px;
    font-weight: 900;
    color: var(--teal);
    letter-spacing: 0.01em;
    line-height: 1;
  }
  .person-title {
    position: absolute;
    left: 65px;
    top: 294px;
    font-size: 21px;
    color: var(--ink);
    line-height: 1;
  }
  .contact-list {
    position: absolute;
    left: 64px;
    top: 336px;
    list-style: none;
  }
  .contact-item {
    display: flex;
    align-items: center;
    height: 33px;
    font-size: 21px;
    color: var(--ink);
  }
  .contact-icon {
    width: 24px;
    height: 24px;
    margin-right: 19px;
    flex: none;
  }
  .offer {
    position: absolute;
    right: 56px;
    top: 248px;
    width: 250px;
    text-align: right;
  }
  .offer-online {
    font-size: 30px;
    font-weight: 900;
    color: var(--orange);
    line-height: 1.1;
  }
  .offer-price {
    margin-top: 10px;
    font-size: 19px;
    font-weight: 700;
    color: var(--teal);
    line-height: 1.3;
  }
  .offer-note {
    margin-top: 8px;
    font-size: 13px;
    color: var(--muted);
    line-height: 1.35;
  }
  .sea-band {
    position: absolute;
    left: 0;
    bottom: 0;
    width: 100%;
    height: 42px;
    background: var(--teal);
  }
</style>
</head>
<body>
  <section class="business-card">
    <h1 class="brand-name">Harborline Cremations</h1>

    <h2 class="person-name">DANIEL REYES</h2>
    <p class="person-title">Founder &amp; CEO</p>

    <ul class="contact-list">
      <li class="contact-item">
        <svg class="contact-icon" viewBox="0 0 24 24" aria-hidden="true">
          <path fill="var(--orange)" d="M6.6 10.8c1.4 2.8 3.8 5.1 6.6 6.6l2.2-2.2c.3-.3.7-.4 1-.2 1.1.4 2.3.6 3.6.6.6 0 1 .4 1 1V20c0 .6-.4 1-1 1C10.6 21 3 13.4 3 4c0-.6.4-1 1-1h3.5c.6 0 1 .4 1 1 0 1.3.2 2.5.6 3.6.1.3 0 .7-.2 1l-2.3 2.2z"/>
        </svg>
        <span>(305) 418-7260</span>
      </li>
      <li class="contact-item">
        <svg class="contact-icon" viewBox="0 0 24 24" aria-hidden="true">
          <rect x="2" y="5" width="20" height="14" rx="1.5" fill="var(--orange)"/>
          <path d="M3 6.5l9 6.5 9-6.5" fill="none" stroke="var(--card)" stroke-width="1.6"/>
        </svg>
        <span>harborlinecremations@mailbox.example</span>
      </li>
      <li class="contact-item">
        <svg class="contact-icon" viewBox="0 0 24 24" aria-hidden="true">
          <g fill="none" stroke="var(--orange)" stroke-width="1.6">
            <circle cx="12" cy="12" r="9"/>
            <ellipse cx="12" cy="12" rx="4" ry="9"/>
            <path d="M3 12h18M4.5 7.5h15M4.5 16.5h15"/>
          </g>
        </svg>
        <span>www.HarborlineCremationsMiami.example</span>
      </li>
    </ul>

    <div class="offer">
      <p class="offer-online">100% Online</p>
      <p class="offer-price">Prices starting at $695 all-inclusive</p>
      <p class="offer-note">(prices subject to change without notice)</p>
    </div>

    <div class="sea-band"></div>
  </section>
</body>
</html>
```